The Gemstone Craft Studio Sales Business Card

The goal of this project is to create a interactive & effective business card design for SALES purposes with the intention to get customer on to our website and make a purchase or contact us about a product or service.
Website: WWW.RINGFORGEHUB.COM
GoogleMyBusiness: https://g.page/RingForgeHUB?gm
Facebook & Instagram: @THEGEMSTONECRAFTSTUDIO
Phone # & Text Message & Whatsapp Message: +1(555) 418-0293
Email: HELLO@RINGFORGEHUB.COM
Location: 4872 Brambleton Avenue Suite 512 Ashgrove Ridge, VT
(It would be necessary to have the appropriate ticker/icon for each social media platform as well as the location ticker and phone / messaging icons instead of spelling the words out.)
It is important to have the company logo and details but with an emphasis toward website. Feel free to also completely make one design your way and completely custom as you feel best.
The Gemstone Craft Studio is a Provider of Luxury Goods & Services such as: Custom Jewelry Design, Jewelry Repairs & Cleaning, Designer Jewelry, Luxury Gifts, 24 Karat Gold, 22 Karat Gold Jewelry, Diamond Jewelry, Insured Jewelry Appraisals, Loose Gemstones & Diamonds, Supporting Sustainability
Target Market(s)
People looking to invest in precious metals and gemstones as well as people looking to find a gift for a loved one for a special occasion. Customers looking to Custom Design Jewelry.
Contact Information for Business Card
Font styles to use
Other font styles liked:
- w.e you want
Colors
Designer to choose colors to be used in the design.
Requirements
Must have
- Website: WWW.RINGFORGEHUB.COM
- GoogleMyBusiness: https://g.page/RingForgeHUB?gm
- Facebook & Instagram: @THEGEMSTONECRAFTSTUDIO
- Phone # & Text Message & Whatsapp Message: +1(555) 418-0293
- Email: HELLO@RINGFORGEHUB.COM
- Location: 4872 Brambleton Avenue Suite 512 Ashgrove Ridge, VT
- (It would be necessary to have the appropriate ticker/icon for each social media platform as well as the location ticker and phone / messaging icons instead of spelling the words out.)
- It is important to have the company logo and details but with an emphasis toward website. Feel free to also completely make one design your way and completely custom as you feel best.
Nice to have
- The Gemstone Craft Studio is a Provider of Luxury Goods & Services such as: Custom Jewelry Design, Jewelry Repairs & Cleaning, Designer Jewelry, Luxury Gifts, 24 Karat Gold, 22 Karat Gold Jewelry, Diamond Jewelry, Insured Jewelry Appraisals, Loose Gemstones & Diamonds, Supporting Sustainability

```html
<!DOCTYPE html>
<html lang="en">
<head>
<meta charset="utf-8">
<title>The Gemstone Craft Studio – Business Card</title>
<link rel="stylesheet" href="https://fonts.googleapis.com/css2?family=Arimo:wght@400&family=Cinzel:wght@500&display=swap">
<style>
  :root {
    --backdrop: #3f3f41;
    --card: #161616;
    --red: #e41b23;
    --gold: #d9ab62;
    --text: #d6d6d6;
    --divider: #2e2e2e;
  }
  * { box-sizing: border-box; margin: 0; padding: 0; }
  html, body { width: 1200px; height: 1200px; overflow: hidden; }
  body {
    background: var(--backdrop);
    font-family: "Arimo", Arial, sans-serif;
    position: relative;
  }
  .card {
    position: absolute;
    left: 250px;
    width: 700px;
    height: 400px;
    background: var(--card);
    border-radius: 100px 6px 100px 6px;
    color: var(--text);
  }
  .card--front { top: 150px; }
  .card--back { top: 640px; }

  /* Front */
  .front-name {
    position: absolute;
    top: 130px; left: 0; right: 0;
    text-align: center;
    font-family: "Cinzel", "Times New Roman", serif;
    font-weight: 500;
    font-size: 40px;
    line-height: 1.25;
    color: var(--red);
  }
  .front-row {
    position: absolute;
    bottom: 48px;
    left: 36px; right: 40px;
    display: flex;
    justify-content: space-between;
    align-items: center;
    font-size: 19px;
    letter-spacing: 0.3px;
  }
  .front-item { display: flex; align-items: center; gap: 8px; }
  .icon-red {
    width: 26px; height: 26px;
    border: 2px solid var(--red);
    border-radius: 50%;
    display: inline-flex; align-items: center; justify-content: center;
  }
  .icon-red svg { width: 14px; height: 14px; fill: var(--red); }

  /* Back */
  .brand-block {
    position: absolute;
    left: 30px; top: 0; bottom: 0;
    width: 290px;
    display: flex; flex-direction: column;
    justify-content: center; align-items: center;
    text-align: center;
  }
  .brand-mark {
    width: 60px; height: 60px;
    border-radius: 50%;
    background: var(--gold);
    margin-bottom: 22px;
  }
  .brand-name {
    font-family: "Cinzel", "Times New Roman", serif;
    font-weight: 500;
    font-size: 30px;
    line-height: 1.15;
    color: var(--red);
  }
  .brand-tagline {
    margin-top: 8px;
    font-family: "Cinzel", "Times New Roman", serif;
    font-size: 14px;
    color: var(--gold);
    letter-spacing: 0.5px;
  }
  .divider {
    position: absolute;
    left: 340px; top: 60px; bottom: 60px;
    width: 1px;
    background: var(--divider);
  }
  .contact-list {
    position: absolute;
    left: 370px; top: 78px; right: 20px;
    list-style: none;
    font-size: 17px;
  }
  .contact-list li {
    display: flex; align-items: center; gap: 12px;
    height: 34px;
    white-space: nowrap;
  }
  .contact-list li.address {
    align-items: flex-start;
    height: auto;
    margin-top: 14px;
    line-height: 1.3;
    white-space: normal;
  }
  .icon-gold {
    flex: none;
    width: 26px; height: 26px;
    border: 2px solid var(--gold);
    border-radius: 50%;
    display: inline-flex; align-items: center; justify-content: center;
  }
  .icon-gold svg { width: 14px; height: 14px; fill: var(--gold); }
  .icon-plain::after {
    content: "";
    width: 10px; height: 10px;
    border-radius: 50%;
    background: var(--gold);
  }
</style>
</head>
<body>

<section class="card card--front">
  <h1 class="front-name">The Gemstone<br>Craft Studio</h1>
  <div class="front-row">
    <span class="front-item">
      <span class="icon-red"><svg viewBox="0 0 16 16"><path d="M1 3h14v10H1z M1 3l7 6 7-6" fill="none" stroke="#e41b23" stroke-width="1.8"/></svg></span>
      HELLO@RINGFORGEHUB.COM
    </span>
    <span class="front-item">
      <span class="icon-red"><svg viewBox="0 0 16 16"><path d="M3 1l3 3-1.5 2a9 9 0 0 0 5.5 5.5L12 10l3 3-2 2C6 15 1 10 1 3z"/></svg></span>
      <span class="icon-red"><svg viewBox="0 0 16 16"><path d="M1 2h14v9H6l-4 3v-3H1z"/></svg></span>
      <span class="icon-red"></span>
      +1(555) 418-0293
    </span>
  </div>
</section>

<section class="card card--back">
  <div class="brand-block">
    <div class="brand-mark"></div>
    <h2 class="brand-name">The Gemstone<br>Craft Studio</h2>
    <p class="brand-tagline">Refined Bespoke Pieces</p>
  </div>
  <div class="divider"></div>
  <ul class="contact-list">
    <li>
      <span class="icon-gold"><svg viewBox="0 0 16 16"><circle cx="8" cy="8" r="6.5" fill="none" stroke="#d9ab62" stroke-width="1.6"/><path d="M1.5 8h13M8 1.5c-3 3.5-3 9.5 0 13M8 1.5c3 3.5 3 9.5 0 13" fill="none" stroke="#d9ab62" stroke-width="1.3"/></svg></span>
      WWW.RINGFORGEHUB.COM
    </li>
    <li><span class="icon-gold icon-plain"></span>https://g.page/RingForgeHUB?gm</li>
    <li><span class="icon-gold icon-plain"></span>@THEGEMSTONECRAFTSTUDIO</li>
    <li><span class="icon-gold icon-plain"></span>@THEGEMSTONECRAFTSTUDIO</li>
    <li class="address">
      <span class="icon-gold"><svg viewBox="0 0 16 16"><path d="M8 1a5 5 0 0 0-5 5c0 4 5 9 5 9s5-5 5-9a5 5 0 0 0-5-5zm0 7a2 2 0 1 1 0-4 2 2 0 0 1 0 4z"/></svg></span>
      <span>4872 Brambleton Avenue Suite 512<br>Ashgrove Ridge, VT</span>
    </li>
  </ul>
</section>

</body>
</html>
```